Breakfast Cafe - The Coral Table

It is for my breakfast and lunch cafe with a hawaiian / beach theme. I am open 7 days a week from 7am to 2pm. We serve traditional American food such as omelettes, pancakes, burgers and sandwiches. I'll upload my old card and my new logo to be used. We have a lot of day to day regulars who eat there during the week, our t-shirts actually say 'Locals Only' on them. Hope this helps. Thanks.

Target Market(s)

anyone who has an appetite!

Industry/Entity Type

American Restaurant

Contact Information for Business Card

4815C Driftwood Shore Road
Long Beach, California
(562) 555-0187

Requirements
Must have
• Address and phone number easily readable.
Nice to have
• beach or tropical theme

```html
<!DOCTYPE html>
<html lang="en">
<head>
<meta charset="utf-8">
<title>The Coral Table – Business Card</title>
<link rel="stylesheet" href="https://fonts.googleapis.com/css2?family=Fredoka:wght@600&family=Righteous&display=swap">
<style>
  :root {
    --page: #ffffff;
    --sky: #9fb6c4;
    --sea: #3f6f86;
    --wood: #6a4128;
    --warm: #c08a5a;
    --sand: #d9b07a;
    --sand-deep: #b98a55;
    --ocean-blue: #8cc6ee;
    --outline: #ffffff;
    --panel: #fff01a;
    --panel-ink: #6a3a1c;
    --emblem: #8a5a2b;
  }
  * { box-sizing: border-box; margin: 0; padding: 0; }
  html, body {
    width: 1200px; height: 900px; overflow: hidden;
    background: var(--page);
  }
  .card {
    position: absolute; left: 129px; top: 181px;
    width: 942px; height: 537px; overflow: hidden;
  }
  .beach-scene {
    position: absolute; inset: 0;
    background:
      radial-gradient(ellipse 38% 30% at 62% 48%, rgba(225,190,90,.85), rgba(225,190,90,0) 70%),
      linear-gradient(180deg, var(--sky) 0%, #b7c3c6 22%, var(--sea) 36%, var(--wood) 50%, var(--warm) 70%, var(--sand) 86%, var(--sand-deep) 100%);
  }
  .brand {
    position: absolute; left: 16px; top: 12px; width: 248px;
    display: flex; flex-direction: column; align-items: center;
  }
  .brand-mark {
    width: 206px; height: 186px; border-radius: 50%;
    background: var(--emblem);
  }
  .brand-name {
    margin-top: 4px;
    font-family: "Fredoka", sans-serif; font-weight: 600;
    font-size: 30px; color: var(--ocean-blue); white-space: nowrap;
  }
  .hours {
    position: absolute; left: 78px; top: 330px;
    transform-origin: left bottom; transform: rotate(-14.8deg);
    font-family: "Fredoka", sans-serif; font-weight: 600;
    font-size: 33px; letter-spacing: 3px; color: var(--ocean-blue);
    text-shadow: -2px -2px 0 var(--outline), 2px -2px 0 var(--outline), -2px 2px 0 var(--outline), 2px 2px 0 var(--outline);
    white-space: nowrap;
  }
  .contact-panel {
    position: absolute; left: 416px; top: 283px;
    width: 502px; height: 150px; border-radius: 22px;
    background: var(--panel);
    padding: 22px 20px 0 0; text-align: right;
    font-family: "Righteous", sans-serif; font-size: 25px;
    line-height: 36px; letter-spacing: 1.6px; color: var(--panel-ink);
  }
  .tagline {
    position: absolute; left: 21px; top: 474px;
    font-family: "Fredoka", sans-serif; font-weight: 600;
    font-size: 27px; letter-spacing: 2px; color: var(--ocean-blue);
    text-shadow: -2px -2px 0 var(--outline), 2px -2px 0 var(--outline), -2px 2px 0 var(--outline), 2px 2px 0 var(--outline);
  }
</style>
</head>
<body>
  <main class="card">
    <div class="beach-scene" role="img" aria-label="Blurred beach photo with a paper cocktail umbrella and tiny deck chairs on sand, sea and parasols behind"></div>

    <div class="brand">
      <div class="brand-mark"></div>
      <div class="brand-name">The Coral Table</div>
    </div>

    <p class="hours">BREAKFAST AND LUNCH 7A.M-2P.M DAILY</p>

    <address class="contact-panel">
      4815C DRIFTWOOD SHORE ROAD<br>
      LONG BEACH, CALIFORNIA 90803<br>
      PHONE: (562) 555-0187
    </address>

    <p class="tagline">FAMILY OWNED AND OPERATED!</p>
  </main>
</body>
</html>
```